Consulting Website

We are looking at renewing out company's website. we are an organizational development consulting firm that works within the Middle East and Africa. Our focus on on organizations within the Gulf area.

We are looking to having a simple, clean and attractive website. pictures should be relevant to our location.

We are also looking for a creative design, something that isn't just "another consulting website"
Updates

Thank you all for submitting your designs, following are some general comments;

- Having a veiled women on the intro is NOT a must
- have a picture with people is NOT a must too, we can use nature, symbols, places..anything really!
- Here are some sites i like;
mivanorth.example
http://www.brellokhomes.example/
http://www.quistavarn.example/
http://www.zorebin.example/

I hope these could give you some idea :)

thanks again.

Industry/Entity Type

It Company

Requirements
Must have
• Tabs for press, testimonials, products, resources and services.
pictures also should be relevant to the geographical location. i.e. veiled women, men in traditional costumes and so on.

It's very important that we MAINTAIN the corporate colors of the logo.
Should not have
• Clean and neat design!
i REALLY dont like crowded designs.

```html
<!DOCTYPE html>
<html lang="en">
<head>
<meta charset="utf-8">
<title>Veranta Consulting</title>
<link href="https://fonts.googleapis.com/css2?family=Source+Sans+3:wght@300;400;600&family=Arimo&display=swap" rel="stylesheet">
<style>
:root{
  --page:#ffffff;
  --brand-slate:#6d8592;
  --brand-rose:#d5a497;
  --brand-sage:#a8b5a4;
  --panel-sand:#cfc1a1;
  --footer-gold:#b3965f;
  --text:#6f6f6f;
  --heading:#5d5d5d;
  --panel-heading:#5a4a2c;
  --panel-link:#7a6a4b;
  --footer-link:#a0865a;
  --light:#ffffff;
}
*{margin:0;padding:0;box-sizing:border-box}
html,body{width:900px;height:1200px;overflow:hidden;background:var(--page)}
body{position:relative;font-family:"Source Sans 3",sans-serif;color:var(--text)}
.abs{position:absolute}

.brand{left:70px;top:48px;display:flex;align-items:center;gap:14px}
.brand-square{width:66px;height:66px;background:var(--brand-rose)}
.brand-name{font-weight:300;font-size:44px;letter-spacing:3px;color:var(--brand-slate);line-height:1}

.social{top:28px;left:674px;display:flex;gap:7px}
.social span{width:32px;height:32px;border-radius:50%;background:#f4f4f4;border:1px solid #dcdcdc;box-shadow:0 1px 2px rgba(0,0,0,.15)}

.search{left:650px;top:102px;width:211px;height:22px;background:var(--brand-sage);display:flex}
.search span{flex:1;color:#eef1ec;font-size:10px;font-style:italic;padding:5px 0 0 16px}
.search button{width:30px;height:22px;border:0;background:#74877a;display:flex;align-items:center;justify-content:center}

.nav{left:42px;top:149px;width:819px;height:29px;background:var(--brand-rose)}
.nav a{position:absolute;top:7px;font-size:12px;color:var(--light);text-decoration:none}
.nav .current{top:-2px;height:33px;width:64px;left:22px;background:var(--brand-sage);text-align:center;padding-top:9px}

.slider{left:57px;top:191px;width:790px;height:267px;background:#fafafa;border:1px solid #dedede;box-shadow:0 10px 14px -8px rgba(0,0,0,.25)}
.slide-photo{left:9px;top:9px;width:772px;height:248px;background:linear-gradient(100deg,#b59a92 0%,#e9dcd6 22%,#8c7570 40%,#efe6e3 55%,#6d5a58 70%,#d9cfd3 88%,#a99ea6 100%)}
.caption{left:9px;top:189px;width:772px;height:68px;background:rgba(240,240,240,.82)}
.caption h2{position:absolute;left:26px;top:10px;font-weight:400;font-size:19px;color:#6a6a6a}
.caption p{position:absolute;left:27px;top:40px;font-family:Arimo,sans-serif;font-size:11.4px;color:#333}
.arrow{top:113px;width:22px;height:30px;background:rgba(255,255,255,.55);display:flex;align-items:center;justify-content:center}
.dots{left:406px;top:474px;display:flex;gap:5px}
.dots span{width:11px;height:11px;border-radius:50%;background:#9a9a9a;box-shadow:inset 0 1px 1px rgba(0,0,0,.3)}
.dots .on{background:#c88e68}

.welcome{left:51px;top:503px;width:545px}
.welcome h1{font-weight:400;font-size:20px;color:var(--heading);margin-bottom:14px}
.welcome p{font-size:9.2px;line-height:15.4px}

.sidebar{left:631px;top:488px;width:230px;height:341px;background:var(--panel-sand)}
.sidebar h3{position:absolute;font-weight:400;font-size:20px;color:var(--panel-heading)}
.sidebar ul{position:absolute;left:22px;list-style:none}
.sidebar li{font-size:11.5px;color:var(--panel-link);line-height:20.6px}
.sidebar li::before{content:"→";font-size:9px;margin-right:8px}
.sidebar hr{position:absolute;left:18px;top:162px;width:192px;border:0;border-top:1px solid #b8a682}

.footer-fade{left:0;top:838px;width:900px;height:32px;background:linear-gradient(#fff,#f3ebdf)}
.footer{left:0;top:870px;width:900px;height:249px;background:var(--footer-gold);color:var(--light)}
.footer h4{position:absolute;top:14px;font-weight:400;font-size:20px;color:#5c4a26}
.pager{position:absolute;top:16px;font-size:18px;color:#5c4a26;letter-spacing:10px}
.press-item{position:absolute;left:53px;width:196px;font-size:9.5px;line-height:15.4px}
.press-item b{display:block;font-weight:400;font-size:15px;line-height:18px}
.press-rule{position:absolute;left:53px;width:196px;border-top:1px solid #cdb88f}
.testi{position:absolute;left:311px;width:268px;font-size:9.3px;line-height:15.4px}
.map{left:649px;top:46px;width:194px;height:86px;background:linear-gradient(135deg,#e3e1dc,#cfccc5 55%,#ebe3c4);border:2px solid #ece4d2}
.contact{left:652px;top:148px;font-size:10px;line-height:15.5px}
.contact td{vertical-align:top}

.bottom-links{left:0;top:1143px;width:900px;text-align:center;font-size:12px;color:var(--footer-link)}
.bottom-links span{margin:0 6px}
.copyright{left:0;top:1167px;width:900px;text-align:center;font-size:9px;color:var(--footer-link)}
</style>
</head>
<body>

<div class="abs brand">
  <div class="brand-square"></div>
  <div class="brand-name">Veranta Consulting</div>
</div>

<div class="abs social" aria-label="Social links">
  <span></span><span></span><span></span><span></span><span></span>
</div>

<div class="abs search">
  <span>Search</span>
  <button aria-label="Search">
    <svg width="12" height="12" viewBox="0 0 12 12"><circle cx="5" cy="5" r="3.5" fill="none" stroke="#2d3a32" stroke-width="1.6"/><line x1="7.6" y1="7.6" x2="11" y2="11" stroke="#2d3a32" stroke-width="2"/></svg>
  </button>
</div>

<nav class="abs nav">
  <a class="current">Home</a>
  <a style="left:124px">About VERANTA</a>
  <a style="left:248px">Offerings</a>
  <a style="left:340px">Knowledge Base</a>
  <a style="left:471px">Contact us</a>
</nav>

<div class="abs slider">
  <div class="abs slide-photo" role="img" aria-label="Photo of women in headscarves gathered in a crowd"></div>
  <div class="abs caption">
    <h2>Lorem Ipsum</h2>
    <p>Lorem ipsum dolor sit amet, consectetuer adipiscing elit, sed diam nonummy nibh euismod tincidunt ut laoreet dolore magna aliquam erat volutpat.</p>
  </div>
  <div class="abs arrow" style="left:9px"><svg width="10" height="12" viewBox="0 0 10 12"><path d="M7 1 2 6l5 5" fill="none" stroke="#fff" stroke-width="2.4"/></svg></div>
  <div class="abs arrow" style="left:759px;background:none"><svg width="10" height="12" viewBox="0 0 10 12"><path d="M3 1l5 5-5 5" fill="none" stroke="#fff" stroke-width="2"/></svg></div>
</div>

<div class="abs dots"><span></span><span></span><span class="on"></span><span></span><span></span><span></span></div>

<section class="abs welcome">
  <h1>Welcome To Veranta Consulting</h1>
  <p>Veranta Consulting is a firm specialized in providing customized Organization Development solutions to companies in the Middle East and Africa. Recognizing the inability of imported models and solutions to solve problems that face companies in our region, Veranta Consulting builds on international best practices and customizes them to create best-fit solutions that are capable of addressing challenges effectively.</p>
  <p>Veranta Consulting provides Organization Development solutions addressing the "HOW – Soft Side" that is needed to achieve the "WHAT – Business Strategy" in a holistic manner. Veranta Consulting work centers around building an organizational culture that is aligned with and supports the business strategy.</p>
  <p>Veranta Consulting helps organization develop an aligned humanistic organization design that:</p>
  <p>o&nbsp;&nbsp;Creates a culture of high performance<br>o&nbsp;&nbsp;Nurtures leaders &amp; builds human potential<br>o&nbsp;&nbsp;Induces innovation across all corporate practices<br>o&nbsp;&nbsp;Increases internal organization efficiencies<br>o&nbsp;&nbsp;Enhances organization agility</p>
  <p>Veranta Consulting utilizes a collaborative consulting model in which consultants work hand in hand with our clients to help them build organizations that support achieving the business strategy. They support clients with the implementation of change initiatives and, most importantly, transfer knowledge and build internal client capability to lead future change programs.</p>
  <p>At Veranta Consulting, we believe that change can only happen when leadership, people and culture within the organization are open and willing to make this change; therefore in our efforts to implement major changes within the organization, Veranta Consulting uses a culture lens as a major mean to see through the organization and makes its organizational change decisions accordingly.</p>
</section>

<aside class="abs sidebar">
  <h3 style="left:22px;top:17px">Products</h3>
  <ul style="top:48px">
    <li>Praesentium voluptatum</li><li>voluptas assumenda</li><li>voluptatibus maiore</li><li>Praesentium voluptatum</li><li>voluptas assumenda</li>
  </ul>
  <hr>
  <h3 style="left:20px;top:172px">Services</h3>
  <ul style="top:207px">
    <li>voluptatibus maiore</li><li>Praesentium voluptatum</li><li>voluptas assumenda</li><li>voluptatibus maiore</li>
  </ul>
</aside>

<div class="abs footer-fade"></div>
<footer class="abs footer">
  <h4 style="left:52px">Press</h4>
  <div class="pager" style="left:206px">&lt;&gt;</div>
  <div class="press-item" style="top:46px"><b>Feb 18</b>Lorem Ipsum is simply dummy text of the printing and typesetting industry.</div>
  <div class="press-rule" style="top:106px"></div>
  <div class="press-item" style="top:116px"><b>Feb 18</b>Lorem Ipsum is simply dummy text of the printing and typesetting industry.</div>
  <div class="press-rule" style="top:174px"></div>
  <div class="press-item" style="top:184px"><b>Feb 18</b>Lorem Ipsum is simply dummy text of the printing and typesetting industry.</div>

  <h4 style="left:310px">Testimonials</h4>
  <div class="pager" style="left:534px">&lt;&gt;</div>
  <p class="testi" style="top:45px">Lorem Ipsum is simply dummy text of the printing and typesetting industry. Lorem Ipsum has been the industry's standard dummy text ever</p>
  <p class="testi" style="top:106px">Lorem Ipsum is simply dummy text of the printing and typesetting industry. Lorem Ipsum has been the industry's standard dummy text ever</p>
  <p class="testi" style="top:167px">Lorem Ipsum is simply dummy text of the printing and typesetting industry. Lorem Ipsum has been the industry's standard dummy text ever</p>

  <h4 style="left:644px">Contact Us</h4>
  <div class="abs map" role="img" aria-label="Street map showing the office location"></div>
  <table class="abs contact">
    <tr><td style="width:60px">Contact Us :</td><td>Veranta Consulting</td></tr>
    <tr><td></td><td>Excepteur sint occaecat<br>cupidatat non<br>eiusmod - 52685</td></tr>
    <tr><td>Call Us</td><td>: 555 014 2290</td></tr>
  </table>
</footer>

<div class="abs bottom-links">Home <span>|</span> About VERANTA <span>|</span> Offerings <span>|</span> Knowledge Base <span>|</span> Contact us</div>
<div class="abs copyright">Copyright@2012 www.verantaconsulting.example</div>

</body>
</html>
```